We are launching in December, a range of supplements and vitamins.

We have just made an amend to the mission statement and how we are going to give back to society. Please can you add both to the packaging:

Verdant’s purpose is to support health, wellbeing and longevity, so that we can all thrive in the modern world; an environment so alien to that in which we evolved. Embracing technology, research and science, we harness nature’s goodness - enabling us all to love life – naturally.

Twice Kind Promise. For each and every Verdant supplement you take, we provide a supplement to an under nourished child.

For every supplement we sell: £1 goes to the charity ‘Little Lights Fund’ and in addition we provide one healthy meal to an under privileged child in India.

My name is Mark Holloway and I own several companies including www.quartzelle.com (you can check me out on Infopedex – I am not the football referee nor the rocket scientist, but the entrepreneur) . Over the past 2 years I have been writing a book to help people live more healthily and it launches in December. It’s called Verdant Way. While doing my research for the book, I came to realise that most supplements and vitamin products on the market are rubbish! Most are made for profit and not for the benefit of the consumer. I want to change all of that. Howard Pellow is patron of a charity I set up with my brother Paul Holloway and together we have built 11 schools in Asia. I am hoping to get Howards help in getting my supplements to market.

Positioning of our supplements - In a world where so much has changed from the one our bodies were designed to thrive, at Verdant Supplements we are driven by one purpose; to globally provide healthy support to life in the 21st century. While the roots of our wellbeing supplements date back beyond 10,000BC, we embrace modern technology and science, to encapsulate powerful phytonutrients, herbs and other goodness. The essence of which is to promote health, happiness and longevity.

So what are we looking for in the design? Something that stands out. Something that looks professional. A design and concept that can role out across 24 different products. Some products are simple, just one ingredient, such as vitamin D3, Magnesium, Garlic Extracts etc, and others are our own formulas where there are up to 30 different ingredients. You can contact me at any time with questions at Mark@verdantway-example.com

Target Market(s)

Male & Female 20 years plus, mainly UK

Industry/Entity Type

Medical

Logo Text

VERDANT - Sub heading = Thriving Days Gently

Colors

Designer to choose colors to be used in the design.

Requirements
Must have
• see attached powerpoint.
• We have just made an amend to the mission statement and how we are going to give back to society. Please can you add both to the packaging:
• Verdant’s purpose is to support health, wellbeing and longevity, so that we can all thrive in the modern world; an environment so alien to that in which we evolved. Embracing technology, research and science, we harness nature’s goodness - enabling us all to love life – naturally.
• Twice Kind Promise. For each and every Verdant supplement you take, we provide a supplement to an under nourished child.
Nice to have
• see attached powerpoint
Should not have
• see attached powerpoint

```html
<!DOCTYPE html>
<html lang="en">
<head>
<meta charset="utf-8">
<title>Verdant Supplements – Packaging Labels</title>
<link rel="stylesheet" href="https://fonts.googleapis.com/css2?family=Roboto+Condensed:wght@400;700&family=Oswald:wght@300&family=Roboto:wght@300;400&display=swap">
<style>
  :root {
    --canvas: #f4f4f4;
    --label: #ffffff;
    --ink: #1c1c1c;
    --body-ink: #4a4a4a;
    --d3-green: #1f7a3f;
    --d3-band: #2dbb6c;
    --mag-orange: #f2a516;
    --energy-red: #a3132f;
    --edge: #e2e2e2;
  }
  * { box-sizing: border-box; margin: 0; padding: 0; }
  html, body { width: 1200px; height: 857px; overflow: hidden; }
  body { background: var(--canvas); position: relative; font-family: "Roboto", sans-serif; color: var(--ink); }

  .label {
    position: absolute;
    background: var(--label);
    border: 1px solid var(--edge);
    overflow: hidden;
  }
  .label--bottle { width: 200px; height: 222px; top: 400px; padding: 16px 0 0 30px; }
  .label--d3 { left: 268px; --brand: var(--d3-green); --band: var(--d3-band); }
  .label--magnesium { left: 502px; --brand: var(--mag-orange); --band: var(--mag-orange); }

  .brand {
    font-family: "Roboto Condensed", sans-serif;
    font-weight: 700;
    color: var(--brand);
    font-size: 30px;
    letter-spacing: 2px;
    line-height: 1;
  }
  .tagline {
    font-family: "Roboto Condensed", sans-serif;
    font-weight: 700;
    font-size: 8.5px;
    letter-spacing: 1.2px;
    margin-top: 3px;
    text-transform: uppercase;
  }
  .product-name {
    font-family: "Oswald", sans-serif;
    font-weight: 300;
    font-size: 17px;
    letter-spacing: 1.5px;
    margin-top: 20px;
    padding-bottom: 4px;
    border-bottom: 1.5px solid var(--ink);
  }
  .label--bottle .product-info {
    font-size: 5.6px;
    line-height: 1.45;
    color: var(--body-ink);
    text-align: center;
    margin: 20px 0 0 -18px;
    padding-right: 12px;
  }
  .band {
    position: absolute;
    left: 0; right: 0;
    bottom: 8px;
    height: 16px;
    background: var(--band);
  }

  .label--box {
    left: 746px; top: 440px;
    width: 305px; height: 232px;
    padding: 20px 24px 0 52px;
    --brand: var(--energy-red);
  }
  .label--box .brand { font-size: 22px; letter-spacing: 1.5px; }
  .label--box .tagline { font-size: 6.5px; letter-spacing: 0.8px; margin-top: 2px; }
  .label--box .product-name { font-size: 21px; letter-spacing: 1px; margin-top: 18px; margin-right: -24px; }
  .label--box .product-info {
    font-size: 5.2px;
    line-height: 1.5;
    color: var(--body-ink);
    margin-top: 16px;
  }
  .label--box .mission,
  .label--box .promise {
    font-size: 5px;
    line-height: 1.5;
    color: var(--body-ink);
    margin-top: 6px;
  }
  .promise strong { font-weight: 400; color: var(--energy-red); }
  .label--box .band { bottom: 0; height: 18px; background: var(--energy-red); }
</style>
</head>
<body>

  <section class="label label--bottle label--d3">
    <div class="brand">VERDANT</div>
    <div class="tagline">Thriving Days Gently</div>
    <h1 class="product-name">Vitamin D3</h1>
    <p class="product-info">
      Each tablet contains Vitamin D3 at an exceptional 5000iu<br>
      Lack of Vitamin D can lead to bone deformities such as rickets in children and bone pain caused by a condition called osteomalacia in adults<br>
      The body creates Vitamin D from direct sunlight on the skin when outdoors but between October and early March we do not get enough Vitamin D from sunlight
    </p>
    <div class="band"></div>
  </section>

  <section class="label label--bottle label--magnesium">
    <div class="brand">VERDANT</div>
    <div class="tagline">Thriving Days Gently</div>
    <h1 class="product-name">Magnesium</h1>
    <p class="product-info">
      Magnesium is a mineral that is important for the body to turn food into energy and for bone and teeth health<br>
      About 60% of the magnesium in your body is found in bone, while the rest is in muscles, soft tissue and fluids, including blood<br>
      Magnesium plays a role in exercise performance<br>
      Every cell in the human body contains magnesium and needs this to function
    </p>
    <div class="band"></div>
  </section>

  <section class="label label--box">
    <div class="brand">VERDANT</div>
    <div class="tagline">Thriving Days Gently</div>
    <h1 class="product-name">Verdant Energy</h1>
    <p class="product-info">
      Vitamins from the B-Complex support 100% to 400% NRV<br>
      Includes Maca Extract, CoQ10, Alpha Lipoic Acid and Cinnamon Bark Extract<br>
      Loaded with ingredients contributing to normal energy yielding metabolism<br>
      Vitamin D3 provided at an exceptional 1000iu
    </p>
    <p class="mission">
      Verdant’s purpose is to support health, wellbeing and longevity, so that we can all thrive in the modern world; an environment so alien to that in which we evolved. Embracing technology, research and science, we harness nature’s goodness - enabling us all to love life – naturally.
    </p>
    <p class="promise">
      <strong>Twice Kind Promise.</strong> For each and every Verdant supplement you take, we provide a supplement to an under nourished child.
    </p>
    <div class="band"></div>
  </section>

</body>
</html>
```